Life Insurance For Real Life

this is a statement I came up with - I am selling insurance based on the fact that I have gone through exactly what insurance can do for everyone: <br/>It’s not “just insurance” it’s a life jacket when you can’t stop the boat from sinking. Think about it…. Will you be safe? Will your family be safe if tragedy takes you away? Who will pay all the expenses if you or your spouse are not here anymore? Believe me, I know. Let me help you take care of the ones you love. <br/>Call me: 555-218-6093, Mae Lin Trost <br/>“REAL LIFE EXPERIENCE FOR REAL LIFE”<br/>

Target Market(s)

New Jersey (USA) seniors ages 65-80.

Industry/Entity Type

Insurance

Colors

Designer to choose colors to be used in the design.

Requirements
Must have
• Good photo of family people who look like they are concerned with family matters - I do not want my name or company name on the first page. I also want a button they can press and get to a second page where they enter contact info and include a email us now type button with a direct email from their device to me.
Nice to have
• maybe an interracial couple with 2-3 kids and a mid-life aged couple - 40-something or so - people who look like they want to make sure their family is safe and taken care of. I am looking to play on emotions to get people to think.
Should not have
• should not have my name or company name

```html
<!DOCTYPE html>
<html lang="en">
<head>
<meta charset="utf-8">
<title>Real Life Experience For Real Life</title>
<link href="https://fonts.googleapis.com/css2?family=Open+Sans:wght@600;700&display=swap" rel="stylesheet">
<style>
  :root {
    --navy: #0d2a6b;
    --red: #b3121b;
    --red-hover: #cc1a24;
    --white: #ffffff;
    --sea-top: #9cc9ea;
    --sea-mid: #2f9fc0;
    --sand: #e6d2b4;
    --warm-light: #f1e6d8;
    --warm-mid: #d8c6b2;
  }
  html, body {
    margin: 0;
    padding: 0;
    overflow: hidden;
    background: var(--white);
  }
  .banner {
    position: relative;
    width: 1200px;
    height: 446px;
    overflow: hidden;
    font-family: "Open Sans", Arial, sans-serif;
    color: var(--white);
  }
  .banner-shapes {
    position: absolute;
    inset: 0;
  }
  .banner-text {
    position: absolute;
    margin: 0;
    white-space: nowrap;
    font-weight: 700;
  }
  .headline {
    left: 428px;
    top: 22px;
    font-size: 24px;
    line-height: 33px;
  }
  .services {
    left: 426px;
    top: 63px;
    font-size: 19.5px;
    line-height: 38px;
  }
  .question-title {
    left: 576px;
    top: 200px;
    transform: translateX(-50%);
    font-size: 26px;
    line-height: 36px;
  }
  .message {
    left: 554px;
    top: 244px;
    transform: translateX(-50%);
    text-align: center;
    font-size: 14.5px;
    line-height: 26px;
  }
  .contact-button {
    position: absolute;
    left: 292px;
    top: 372px;
    width: 488px;
    height: 74px;
    padding-left: 16px;
    box-sizing: border-box;
    display: flex;
    align-items: center;
    justify-content: center;
    background: var(--red);
    clip-path: polygon(42px 0, 488px 0, 465px 100%, 0 100%);
    color: var(--white);
    text-decoration: none;
    font-size: 22px;
    font-weight: 700;
    white-space: nowrap;
  }
  .contact-button:hover {
    background: var(--red-hover);
  }
</style>
</head>
<body>
<div class="banner">
  <svg class="banner-shapes" width="1200" height="446" viewBox="0 0 1200 446" xmlns="http://www.w3.org/2000/svg">
    <defs>
      <linearGradient id="beach-tones" x1="0" y1="0" x2="0" y2="1">
        <stop offset="0" stop-color="var(--sea-top)"/>
        <stop offset="0.55" stop-color="var(--sea-mid)"/>
        <stop offset="1" stop-color="var(--sand)"/>
      </linearGradient>
      <linearGradient id="couple-tones" x1="0" y1="0" x2="1" y2="1">
        <stop offset="0" stop-color="var(--warm-light)"/>
        <stop offset="1" stop-color="var(--warm-mid)"/>
      </linearGradient>
    </defs>
    <polygon class="photo-beach" role="img" aria-label="Photo: a father walking hand in hand with his young daughter along the beach" points="0,0 418,0 220,446 0,446" fill="url(#beach-tones)"/>
    <polygon class="stripe-left" points="400,0 418,0 220,446 206,446" fill="var(--red)"/>
    <polygon class="panel" points="418,0 920,0 762,446 220,446" fill="var(--navy)"/>
    <polygon class="stripe-right" points="920,0 934,0 774,446 760,446" fill="var(--red)"/>
    <polygon class="photo-couple" role="img" aria-label="Photo: a smiling senior couple embracing outdoors" points="934,0 1200,0 1200,446 774,446" fill="url(#couple-tones)"/>
  </svg>

  <p class="banner-text headline">REAL LIFE EXPERIENCE FOR REAL LIFE</p>
  <p class="banner-text services">Specilizing in Mortgage Insurance,<br>Whole Life, Term, Universal, Final Expense<br>and Guarnteed Issue Products.</p>
  <p class="banner-text question-title">Think about it.... Will you be safe?</p>
  <p class="banner-text message">Will your family be safe if tragedy takes you away?<br>Who will pay all&nbsp; the expenses if you or your spouse are not here<br>anymore?&nbsp; Believe me, I know.<br>Let me help you take care of the ones you love.</p>
  <a class="contact-button" href="mailto:?subject=Insurance%20inquiry">Call me: 555-218-6093 - Email Me Now</a>
</div>
</body>
</html>
```